Letterhead for a German Distribution/Manufacturing Company

We need a professional Letterhead in a unique Design.
not to playful.
The Letterhead has to show show that we are a international company with headquater in Germany.
all details like adress, Vat Tax Number, Bank Accout, Eori, email, Company number has to be on the Letterhead.
for example use: VAT TAX DE5704168 Bank Account: Norrfeld Bank IBAN DE421705238ß310482 Swift: KOLV3154802 EORI 3041296587 Company Number: HRB 61508 Adress: VOLTRINA UG Amsel Strasse 7 Postal Code 04683 City Halvenstadt Country: Germany Email: info@voltrina-example.com
the design can be colored but doesnt have to be
Industry/Entity Type
Manufacturing and international distribution
Requirements
Must have
- show that we are a international company with headquater in Germany. our company infos and logo

```html
<!DOCTYPE html>
<html lang="en">
<head>
<meta charset="utf-8">
<title>VOLTRINA UG – Letterhead</title>
<link rel="stylesheet" href="https://fonts.googleapis.com/css2?family=Saira:wght@400;600&display=swap">
<style>
  :root {
    --paper: #ffffff;
    --ink: #2b2b2b;
    --band-dark: #5d5d5d;
    --band-light: #ababab;
  }
  * { margin: 0; padding: 0; box-sizing: border-box; }
  html, body {
    width: 919px;
    height: 1200px;
    overflow: hidden;
    background: var(--paper);
  }
  .letterhead {
    position: relative;
    width: 919px;
    height: 1200px;
    background: var(--paper);
    font-family: "Saira", sans-serif;
    color: var(--ink);
  }
  .corner-bands {
    position: absolute;
    inset: 0;
    width: 100%;
    height: 100%;
  }
  .brand {
    position: absolute;
    left: 51px;
    top: 48px;
    display: flex;
    align-items: center;
    gap: 8px;
  }
  .brand-dot {
    width: 62px;
    height: 62px;
    border-radius: 50%;
    background: var(--ink);
  }
  .brand-name {
    font-size: 40px;
    font-weight: 400;
    letter-spacing: 0.5px;
    line-height: 1;
  }
  .contact-block,
  .registry-block {
    position: absolute;
    text-align: right;
    font-size: 15px;
    font-weight: 400;
    letter-spacing: 0.9px;
    font-style: normal;
    white-space: nowrap;
  }
  .contact-block { right: 50px; top: 50px; line-height: 29px; }
  .registry-block { right: 42px; top: 1059px; line-height: 27px; }
  .label { font-weight: 600; }
</style>
</head>
<body>
  <main class="letterhead">
    <svg class="corner-bands" viewBox="0 0 1277 1806" preserveAspectRatio="none" aria-hidden="true">
      <path fill="var(--band-light)" d="M890 0 L990 0 L1040 40 Q1050 50 1065 50 L990 50 Q965 50 950 38 Z"/>
      <path fill="var(--band-dark)" d="M987 0 L1277 0 L1277 258 L1240 214 Q1226 197 1226 175 L1226 50 L1065 50 Q1050 50 1038 40 Z"/>
      <path fill="var(--band-light)" d="M387 1806 L287 1806 L237 1766 Q227 1756 212 1756 L287 1756 Q312 1756 327 1768 Z"/>
      <path fill="var(--band-dark)" d="M290 1806 L0 1806 L0 1548 L37 1592 Q51 1609 51 1631 L51 1756 L212 1756 Q227 1756 239 1766 Z"/>
    </svg>

    <header class="brand">
      <span class="brand-dot"></span>
      <span class="brand-name">VOLTRINA</span>
    </header>

    <address class="contact-block">
      <p><span class="label">Address :</span> VOLTRINA UG Amsel Strasse 7 Postal</p>
      <p>Code 04683 City Halvenstadt Country : Germany</p>
      <p><span class="label">Email :</span> info@voltrina-example.com</p>
    </address>

    <footer class="registry-block">
      <p><span class="label">VAT TAX :</span>&nbsp; DE5704168</p>
      <p><span class="label">Company Number :</span> HRB 61508</p>
      <p><span class="label">Swift :</span> KOLV3154802 EORI 3041296587</p>
      <p><span class="label">Bank Account :</span> Norrfeld Bank IBAN DE421705238ß310482</p>
    </footer>
  </main>
</body>
</html>
```